DESSERT FLYER

We need a flyer design for desserts and drinks for our restaurant.

We use Retro/rustic as main theme

Flyer must include all images, which are attached to this project. We also named correctly for each images, so you can use for each dish's title (docx file)
Must include our logo as well.

Flyer tittle is "SWEET PLUMO"

Please see our website for reference at brickhollow.com.au

Flyer's printing size is A5 Vertical. Single Side

```html
<!DOCTYPE html>
<html lang="en">
<head>
<meta charset="utf-8">
<title>Sweet Plumo – Dessert Flyer</title>
<link rel="stylesheet" href="https://fonts.googleapis.com/css2?family=Luckiest+Guy&family=Gochi+Hand&display=swap">
<style>
  :root {
    --stage: #4b4b4b;
    --gutter: #0b0b0b;
    --label-red: #c8161d;
    --label-plum: #3a1f3d;
    --teal: #2b8f9a;
    --teal-dark: #1d6e77;
    --ink: #1f3a40;
    --white: #ffffff;
    --blue: #1f4fb4;
    --aqua: #2a9fb8;
    --orange: #e07a12;
    --dark: #3a2a22;
    --label-font: "Luckiest Guy", "Arial Black", sans-serif;
    --hand-font: "Gochi Hand", cursive;
  }
  * { margin: 0; padding: 0; box-sizing: border-box; }
  html, body { width: 1200px; height: 745px; overflow: hidden; }
  body { background: var(--stage); position: relative; }

  .flyer {
    position: absolute;
    left: 352px; top: 22px;
    width: 495px; height: 700px;
    background: var(--gutter);
    box-shadow: 0 10px 30px rgba(0,0,0,.5);
    overflow: hidden;
  }
  .flyer__panels { position: absolute; inset: 0; }

  .dish-label {
    position: absolute;
    font-family: var(--label-font);
    font-size: 13px;
    line-height: 1.3;
    letter-spacing: .5px;
    color: var(--white);
    text-transform: uppercase;
    white-space: nowrap;
  }
  .dish-label span {
    padding: 1px 3px;
    border-radius: 4px;
    -webkit-box-decoration-break: clone;
    box-decoration-break: clone;
  }
  .dish-label--red span { background: var(--label-red); }
  .dish-label--plum { text-align: right; }
  .dish-label--plum span { background: var(--label-plum); }

  .label-coconut { left: 12px; top: 132px; }
  .label-rice { right: 12px; top: 18px; }
  .label-icecream { left: 30px; top: 306px; }
  .label-icecream .c-aqua { background: var(--aqua); }
  .label-icecream .c-blue { background: var(--blue); }
  .label-icecream .c-orange { background: var(--orange); }
  .label-icecream .c-dark { background: var(--dark); }
  .label-icecream .c-red { background: var(--label-red); }
  .label-icecream .plain { background: none; text-shadow: 0 0 3px #000; }
  .label-banana { left: 14px; top: 650px; font-size: 14px; }
  .label-coffee { right: 20px; top: 650px; }

  .brand {
    position: absolute; left: 146px; top: 104px;
    width: 150px; height: 52px;
    padding: 0 12px;
    background: var(--white);
    border-radius: 3px;
    box-shadow: 0 2px 6px rgba(0,0,0,.3);
    display: flex; align-items: center; justify-content: center;
    font-family: var(--label-font);
    font-size: 15px; line-height: 1;
    white-space: nowrap;
    color: var(--teal-dark);
    letter-spacing: 1px;
  }
  .title-cloud { position: absolute; left: 118px; top: 170px; width: 245px; height: 95px; }
  .title {
    position: absolute; left: 118px; top: 180px; width: 245px;
    text-align: center;
    font-family: var(--hand-font);
    font-weight: 400;
    font-size: 36px; line-height: 37px;
    color: var(--ink);
  }
  .special-tag {
    position: absolute; left: 283px; top: 244px;
    padding: 2px 18px 4px;
    background: var(--label-red);
    border-radius: 6px;
    transform: rotate(-8deg);
    font-family: var(--hand-font);
    font-size: 28px; line-height: 34px; color: var(--white);
  }
</style>
</head>
<body>
<main class="flyer">
  <svg class="flyer__panels" viewBox="0 0 495 700" width="495" height="700">
    <defs>
      <linearGradient id="tone-coconut" x1="0" y1="0" x2="1" y2="1">
        <stop offset="0" stop-color="#c98a8f"/><stop offset=".45" stop-color="#efe6d6"/><stop offset="1" stop-color="#cfc2a6"/>
      </linearGradient>
      <linearGradient id="tone-rice" x1="0" y1="0" x2="1" y2="0">
        <stop offset="0" stop-color="#4a2a45"/><stop offset=".55" stop-color="#6e5070"/><stop offset="1" stop-color="#f0c640"/>
      </linearGradient>
      <linearGradient id="tone-icecream" x1="0" y1="0" x2="1" y2="0">
        <stop offset="0" stop-color="#5a6a4a"/><stop offset=".45" stop-color="#d99840"/><stop offset=".7" stop-color="#eee9df"/><stop offset="1" stop-color="#8c8f92"/>
      </linearGradient>
      <linearGradient id="tone-banana" x1="0" y1="0" x2="1" y2="1">
        <stop offset="0" stop-color="#f2efe8"/><stop offset=".45" stop-color="#d08a35"/><stop offset="1" stop-color="#3f7a2a"/>
      </linearGradient>
      <linearGradient id="tone-coffee" x1="0" y1="0" x2="1" y2="1">
        <stop offset="0" stop-color="#d8c8b0"/><stop offset=".5" stop-color="#9a7a58"/><stop offset="1" stop-color="#4a3322"/>
      </linearGradient>
    </defs>
    <path role="img" aria-label="Photo: fresh young coconut with straw and lemon slice" fill="url(#tone-coconut)" d="M0 0 H205 Q186 110 198 212 L0 216 Z"/>
    <path role="img" aria-label="Photo: black sticky rice with sliced mango" fill="url(#tone-rice)" d="M216 0 H495 V236 Q362 250 246 202 Q202 100 216 0 Z"/>
    <path role="img" aria-label="Photo: fried ice-cream in a glass bowl" fill="url(#tone-icecream)" d="M0 228 Q250 200 495 252 V394 Q262 440 0 392 Z"/>
    <path role="img" aria-label="Photo: banana fritters and samosa on a banana leaf" fill="url(#tone-banana)" d="M0 404 Q130 420 262 426 V700 H0 Z"/>
    <path role="img" aria-label="Photo: Vietnamese drip coffee being poured" fill="url(#tone-coffee)" d="M272 426 Q390 420 495 406 V700 H272 Z"/>
  </svg>

  <div class="dish-label dish-label--red label-coconut">
    <span>Fresh young</span><br><span>coconut juice</span><br><span>$5.50</span>
  </div>

  <div class="dish-label dish-label--plum label-rice">
    <span>Black sticky rice</span><br><span>with mango</span><br><span>$6.90</span>
  </div>

  <div class="brand">BRICK HOLLOW</div>

  <svg class="title-cloud" viewBox="0 0 245 95" width="245" height="95" aria-hidden="true">
    <path fill="var(--teal)" stroke="#fff" stroke-width="3"
      d="M30 22 Q40 4 70 10 Q95 -2 125 8 Q160 -2 190 10 Q225 6 232 30 Q248 48 232 64 Q230 88 198 84 Q170 96 140 86 Q110 96 80 86 Q48 94 30 78 Q2 72 10 50 Q0 30 30 22 Z"/>
  </svg>
  <h1 class="title">Sweet<br>Plumo</h1>
  <div class="special-tag">Special</div>

  <div class="dish-label label-icecream">
    <span class="c-aqua">Fried ice-cream</span> <span class="c-blue">with</span><br>
    <span class="c-orange">caramel/</span> <span class="c-dark">chocolate/</span><br>
    <span class="c-red">strawberry topping</span><br>
    <span class="plain">$6.90</span>
  </div>

  <div class="dish-label dish-label--red label-banana">
    <span>Banana fritter with</span><br><span>vanilla ice-cream $6.90</span>
  </div>

  <div class="dish-label dish-label--plum label-coffee">
    <span>Vietnamese coffee</span><br><span>$6.90</span>
  </div>
</main>
</body>
</html>
```